8 x 8 Social Media Design - Tax, Accounting & Bookkeeping Service

Bright Ledger Advisory Group, Inc.

Tax, Accounting and Bookkeeping Services

“We provide our services, with you next mortgage in mind”

Special pricing available for all Mortgage Loan Customers!!

President / CEO Marcus Delaney

Primary service provider with over 27 years of experience

Call directly for more information: (555) 284-9037

Or email at: mdelaney@brightledgerhq.example

```html
<!DOCTYPE html>
<html lang="en">
<head>
<meta charset="utf-8">
<title>Bright Ledger Advisory Group – Social Post</title>
<link rel="stylesheet" href="https://fonts.googleapis.com/css2?family=Anton&family=Montserrat:wght@400;500&family=Poppins:wght@400;500;600;700;800&display=swap">
<style>
  :root {
    --navy: #35336b;
    --ink: #1d1d1f;
    --gray-text: #333338;
    --gold: #c8913a;
    --orange: #d9962f;
    --blue-light: #6f9bd6;
    --blue: #3f5fc0;
    --blue-deep: #283a9e;
    --paper: #ececec;
    --paper-shade: #dedede;
    --white: #ffffff;
  }
  * { box-sizing: border-box; margin: 0; padding: 0; }
  html, body {
    width: 1200px; height: 1141px; overflow: hidden;
    background: var(--paper);
  }
  .post {
    position: relative; width: 1200px; height: 1141px; overflow: hidden;
    background: linear-gradient(135deg, #f1f1f1 0%, var(--paper) 55%, var(--paper-shade) 100%);
    font-family: "Montserrat", sans-serif; color: var(--ink);
  }
  .post__art { position: absolute; inset: 0; }
  .brand {
    position: absolute; left: 88px; top: 120px; width: 300px;
    text-align: center;
    font-family: "Poppins", sans-serif; font-weight: 700;
    font-size: 27px; line-height: 1.2; color: var(--navy);
  }
  .brand__dot {
    display: block; width: 22px; height: 22px; margin: 0 auto 10px;
    border-radius: 50%; background: var(--gold);
  }
  .services-line {
    position: absolute; left: 27px; top: 273px;
    font-size: 17px; font-weight: 500; color: var(--ink);
  }
  .headline {
    position: absolute; left: 27px; top: 302px;
    font-family: "Anton", sans-serif; font-weight: 400;
    font-size: 56px; color: var(--navy);
    letter-spacing: 1.5px;
  }
  .headline__line {
    display: block; height: 66px; line-height: 66px; white-space: nowrap;
  }
  .headline__mark {
    display: inline-block; vertical-align: middle;
    line-height: 62px; height: 62px;
    background: var(--navy); color: var(--white);
    padding: 0 5px;
  }
  .provider {
    position: absolute; left: 37px; top: 584px;
    font-size: 28px; line-height: 39px; font-weight: 500; color: var(--gray-text);
  }
  .years__num {
    position: absolute; left: 33px; top: 668px;
    font-family: "Poppins", sans-serif; font-weight: 600;
    font-size: 118px; line-height: 1; color: var(--gold); letter-spacing: -4px;
  }
  .years__unit {
    position: absolute; left: 40px; top: 788px;
    font-size: 31px; font-weight: 400; color: var(--ink);
  }
  .years__rule {
    position: absolute; left: 185px; top: 675px; width: 3px; height: 120px;
    background: var(--navy);
  }
  .years__label {
    position: absolute; left: 205px; top: 688px;
    font-size: 35px; line-height: 57px; font-weight: 400; color: var(--ink);
  }
  .offer {
    position: absolute; left: 41px; top: 842px; width: 460px;
    font-family: "Poppins", sans-serif; font-weight: 700;
    font-size: 28px; line-height: 38px; color: var(--gray-text);
  }
  .offer__accent { color: var(--gold); }
  .contact__lead {
    position: absolute; left: 41px; top: 968px;
    font-family: "Poppins", sans-serif; font-weight: 400; font-size: 22px; color: var(--ink);
  }
  .contact__phone {
    position: absolute; left: 37px; top: 1003px;
    font-family: "Poppins", sans-serif; font-weight: 600; font-size: 44px; color: var(--ink);
  }
  .contact__email {
    position: absolute; left: 47px; top: 1065px;
    font-family: "Poppins", sans-serif; font-weight: 600; font-size: 20px; color: var(--ink);
  }
  .ceo {
    position: absolute; left: 598px; top: 1012px; width: 240px;
    text-align: center;
    font-family: "Poppins", sans-serif; font-weight: 700;
    font-size: 22px; line-height: 29px; color: var(--white);
  }
</style>
</head>
<body>
<main class="post">
  <svg class="post__art" width="1200" height="1141" viewBox="0 0 1200 1141">
    <defs>
      <linearGradient id="band-blue" x1="0" y1="0" x2="0.3" y2="1">
        <stop offset="0" stop-color="#3f5fc0"/>
        <stop offset="0.35" stop-color="#6f9bd6"/>
        <stop offset="1" stop-color="#283a9e"/>
      </linearGradient>
      <linearGradient id="home-photo" x1="0" y1="0" x2="0" y2="1">
        <stop offset="0" stop-color="#6b5644"/>
        <stop offset="0.45" stop-color="#a38a74"/>
        <stop offset="1" stop-color="#5f6a5a"/>
      </linearGradient>
      <linearGradient id="ceo-photo" x1="0" y1="0" x2="0" y2="1">
        <stop offset="0" stop-color="#2a2a2e"/>
        <stop offset="1" stop-color="#141416"/>
      </linearGradient>
    </defs>
    <path class="band band--orange" d="M718 0 C560 300 560 760 1110 1141 L1200 1141 L1200 0 Z" fill="var(--orange)"/>
    <path class="band band--blue" d="M728 0 C598 320 640 800 1200 1141 L1200 0 Z" fill="url(#band-blue)"/>
    <path class="photo photo--home" role="img" aria-label="Photo of a couple standing arm in arm, looking at the front porch of their new house"
          d="M745 0 C664 280 760 720 1200 917 L1200 0 Z" fill="url(#home-photo)"/>
    <path class="photo photo--ceo" role="img" aria-label="Portrait of the company president in a dark coat, hat and glasses"
          d="M560 1141 L585 1060 C600 1010 640 990 665 975 L690 905 C700 880 740 875 760 900 L790 975 C830 995 855 1020 868 1060 L890 1141 Z"
          fill="url(#ceo-photo)"/>
  </svg>

  <div class="brand">
    <span class="brand__dot"></span>
    Bright Ledger Advisory Group, Inc.
  </div>

  <p class="services-line">Tax, Accounting and Bookkeeping Services</p>

  <h1 class="headline">
    <span class="headline__line">We provide</span>
    <span class="headline__line">our services</span>
    <span class="headline__line">with <span class="headline__mark">you next</span></span>
    <span class="headline__line"><span class="headline__mark">mortgage</span> in mind</span>
  </h1>

  <p class="provider">Primary service<br>provider with over:</p>

  <div class="years">
    <span class="years__num">27</span>
    <span class="years__unit">YEARS</span>
    <span class="years__rule"></span>
    <span class="years__label">OF<br>EXPERIENCE</span>
  </div>

  <p class="offer">Special pricing available<br>for all <span class="offer__accent">Mortgage Loan<br>Customers!!</span></p>

  <p class="contact__lead">Call directly for more information:</p>
  <p class="contact__phone">(555) 284-9037</p>
  <p class="contact__email">Or email at: mdelaney@brightledgerhq.example</p>

  <p class="ceo">President / CEO<br>Marcus Delaney</p>
</main>
</body>
</html>
```